TVQ-Business Card Design

I need a modern, professional business card design that includes my logo as the main feature, maybe the entire background with the contact info overlaying or even contact info on the back and the logo full frontal

Neat and organized placement of contact information

Would like to see options in black and white

Target Market(s)

real estate Developers, Construction managers, business and home owners

Industry/Entity Type

Construction

Contact Information for Business Card

TVQ Construction
Dennis Fairweather
General Contractor

Office: 1-888-902-7351 Ext #1
Cell: 412-730-2168
Fax: 1-888-902-7351

Font styles to use
Serif

Requirements
Must have
• title
• office #
• cell #
• Email
• website
Nice to have
• fax

```html
<!DOCTYPE html>
<html lang="en">
<head>
<meta charset="utf-8">
<title>TVQ Construction – Business Cards</title>
<link href="https://fonts.googleapis.com/css2?family=Arimo:wght@400;700&family=Saira+Semi+Condensed:wght@600;700&display=swap" rel="stylesheet">
<style>
  :root {
    --backdrop: #3f5a44;
    --ink: #000000;
    --paper: #ffffff;
    --lime: #8cc63f;
    --lime-dark: #3d9a3a;
    --text-dark: #222222;
    --text-light: #ffffff;
  }
  * { box-sizing: border-box; margin: 0; padding: 0; }
  html, body {
    width: 1200px; height: 800px; overflow: hidden;
    background: var(--backdrop);
  }
  .canvas {
    position: relative; width: 1200px; height: 800px;
    display: flex; align-items: center; justify-content: center; gap: 60px;
  }
  .card {
    position: relative; width: 500px; height: 290px; overflow: hidden;
    box-shadow: 0 14px 30px rgba(0,0,0,.35);
  }

  /* Front */
  .card-front { background: var(--ink); }
  .front-brand {
    position: absolute; left: 0; right: 0; top: 62px;
    display: flex; align-items: center; justify-content: center; gap: 14px;
  }
  .brand-mark { width: 22px; height: 22px; background: var(--lime); }
  .brand-name {
    font-family: "Saira Semi Condensed", sans-serif; font-weight: 700;
    font-size: 78px; line-height: 1; color: var(--lime); letter-spacing: 2px;
  }
  .front-band {
    position: absolute; left: 0; right: 0; top: 178px; height: 58px;
    background: var(--lime);
    border-top: 5px solid var(--lime-dark); border-bottom: 5px solid var(--lime-dark);
    display: flex; align-items: center; padding-left: 78px;
  }
  .front-band-title {
    font-family: "Saira Semi Condensed", sans-serif; font-weight: 600;
    font-size: 34px; color: var(--text-light); letter-spacing: .5px;
  }

  /* Back */
  .card-back { background: var(--paper); }
  .back-bar {
    position: absolute; left: 150px; top: 28px; width: 320px; height: 40px;
    background: var(--lime);
  }
  .back-block {
    position: absolute; right: 0; top: 118px; width: 58px; height: 30px;
    background: var(--lime);
  }
  .holder {
    position: absolute; left: 34px; top: 82px;
    font-family: Arimo, sans-serif; color: var(--text-dark);
  }
  .holder-name { font-weight: 700; font-size: 25px; letter-spacing: .3px; text-transform: uppercase; }
  .holder-title { font-size: 15px; color: #444; }
  .back-brand {
    position: absolute; right: 70px; top: 104px;
    display: flex; align-items: center; gap: 6px;
  }
  .back-brand .brand-mark { width: 9px; height: 9px; }
  .back-brand .brand-name { font-size: 34px; letter-spacing: 1px; }
  .back-contact {
    position: absolute; left: 0; right: 0; bottom: 0; height: 140px;
    background: var(--ink); color: var(--text-light);
    font-family: Arimo, sans-serif; font-size: 13px;
    display: flex; justify-content: space-between;
    padding: 22px 28px 0 34px;
  }
  .contact-list { list-style: none; display: flex; flex-direction: column; gap: 9px; }
  .contact-list--right { padding-top: 50px; }
  .contact-item { display: flex; align-items: center; gap: 9px; }
  .contact-icon { width: 13px; height: 13px; fill: var(--text-light); flex: none; }
</style>
</head>
<body>
<main class="canvas">

  <section class="card card-front" aria-label="Business card front">
    <div class="front-brand">
      <span class="brand-mark"></span>
      <span class="brand-name">TVQ</span>
    </div>
    <div class="front-band">
      <h1 class="front-band-title">TVQ CONSTRUCTION</h1>
    </div>
  </section>

  <section class="card card-back" aria-label="Business card back">
    <div class="back-bar"></div>
    <div class="back-block"></div>
    <div class="holder">
      <h2 class="holder-name">Dennis Fairweather</h2>
      <p class="holder-title">General Contractor</p>
    </div>
    <div class="back-brand">
      <span class="brand-mark"></span>
      <span class="brand-name">TVQ</span>
    </div>
    <div class="back-contact">
      <ul class="contact-list">
        <li class="contact-item">
          <svg class="contact-icon" viewBox="0 0 16 16"><path d="M2 4c0-1 1-2 6-2s6 1 6 2v2h-3V4.5H5V6H2zM4 8l2-2h4l2 2v5H4z"/></svg>
          1-888-902-7351 Ext #1
        </li>
        <li class="contact-item">
          <svg class="contact-icon" viewBox="0 0 16 16"><path d="M4 1h8v4H4zM1 6h14v6h-3v3H4v-3H1zM5 10v4h6v-4z"/></svg>
          1-888-902-7351
        </li>
        <li class="contact-item">
          <svg class="contact-icon" viewBox="0 0 16 16"><path d="M1 2h14v10H9v2h2v1H5v-1h2v-2H1zm1.5 1.5v7h11v-7z"/></svg>
          www.tvqconstruction.com
        </li>
      </ul>
      <ul class="contact-list contact-list--right">
        <li class="contact-item">
          <svg class="contact-icon" viewBox="0 0 16 16"><path d="M4 0h8v16H4zm1.5 1.5v11h5v-11zM7 13.5v1h2v-1z"/></svg>
          412-730-2168
        </li>
        <li class="contact-item">
          <svg class="contact-icon" viewBox="0 0 16 16"><path d="M1 3h14v10H1zm1.5 1.6v.2L8 9l5.5-4.2v-.2zM2.5 6.6v4.9h11V6.6L8 10.8z"/></svg>
          dennis@tvqconstruction.com
        </li>
      </ul>
    </div>
  </section>

</main>
</body>
</html>
```